Whitmore Business Card Design

The name of the business is Dara Whitmore, CPA LLC
The service that we offer is Accounting, Tax & Consulting Services. I need it to have the following items:
Dara Whitmore, Principal
Phone Number
Email Address
Physical Address

I have attached the company logo, one in black and one in white. Please provide a design in black background and the other in white background. Please include "Accounting, Tax & Consulting Services". I want the business card to be clean and very professional.

```html
<!DOCTYPE html>
<html lang="en">
<head>
<meta charset="utf-8">
<title>Dara Whitmore, CPA LLC — Business Card</title>
<link rel="stylesheet" href="https://fonts.googleapis.com/css2?family=Poppins:wght@400;500;700&display=swap">
<style>
  :root {
    --canvas: #ffffff;
    --card-white: #ffffff;
    --charcoal: #38383a;
    --charcoal-back: #3a3a3c;
    --crimson: #9b1a1e;
    --ink: #3d3d3f;
    --muted: #8a8a8c;
    --shadow: rgba(0, 0, 0, 0.35);
  }
  * { margin: 0; padding: 0; box-sizing: border-box; }
  html, body {
    width: 1200px; height: 2400px; overflow: hidden;
    background: var(--canvas);
    font-family: "Poppins", sans-serif;
  }
  .canvas { position: relative; width: 1200px; height: 2400px; }
  .card {
    position: absolute; left: 140px; width: 919px; height: 525px;
    box-shadow: 8px 14px 22px var(--shadow);
    overflow: hidden;
  }
  .card--front { top: 660px; background: var(--card-white); }
  .card--back { top: 1250px; background: var(--charcoal-back); }

  .band { position: absolute; background: var(--charcoal); }
  .band--red { background: var(--crimson); }

  .brand { position: absolute; display: flex; align-items: center; gap: 12px; }
  .brand__mark { width: 14px; height: 14px; background: var(--crimson); }
  .brand__name { font-weight: 500; font-size: 19px; letter-spacing: 0.3px; line-height: 1; }
  .brand__tag { font-weight: 500; font-size: 12.5px; letter-spacing: 1.6px; line-height: 1; margin-top: 5px; }

  .card--front .brand { left: 160px; top: 118px; }
  .card--front .brand__name { color: var(--ink); }
  .card--front .brand__tag { color: var(--muted); }

  .card--back .brand { left: 0; right: 0; top: 255px; justify-content: center; flex-direction: column; gap: 0; text-align: center; }
  .card--back .brand__name { color: #ffffff; font-size: 19px; }
  .card--back .brand__tag { color: #ffffff; margin-top: 6px; }

  .details { position: absolute; left: 235px; top: 262px; color: var(--ink); }
  .details__service {
    color: var(--crimson); font-weight: 700; font-size: 18px; line-height: 22px;
    letter-spacing: 0.6px; text-transform: uppercase;
  }
  .details__person { font-size: 18px; margin-top: 8px; line-height: 24px; }
  .details__list { list-style: none; margin-top: 12px; }
  .details__list li { display: flex; align-items: center; gap: 12px; font-size: 18px; line-height: 26px; }
  .details__list svg { width: 18px; height: 18px; flex: none; }
</style>
</head>
<body>
<main class="canvas">

  <section class="card card--front" aria-label="Business card, front">
    <div class="band" style="left:58px; top:43px; width:432px; height:44px;"></div>
    <div class="band" style="left:58px; top:43px; width:46px; height:167px;"></div>

    <div class="brand">
      <span class="brand__mark"></span>
      <div>
        <div class="brand__name">DARA WHITMORE, CPA, LLC</div>
        <div class="brand__tag">CERTIFIED PUBLIC ACCOUNTANT</div>
      </div>
    </div>

    <div class="band band--red" style="left:58px; top:272px; width:119px; height:28px;"></div>
    <div class="band band--red" style="left:58px; top:333px; width:119px; height:28px;"></div>
    <div class="band band--red" style="left:58px; top:393px; width:119px; height:28px;"></div>

    <div class="details">
      <h1 class="details__service">Accounting, Tax &amp;<br>Consulting Services</h1>
      <p class="details__person">Dara Whitmore, Principal</p>
      <ul class="details__list">
        <li>
          <svg viewBox="0 0 24 24" fill="none" stroke="#3d3d3f" stroke-width="1.6"><path d="M5 3h4l2 5-2.5 1.5a11 11 0 0 0 6 6L16 13l5 2v4a2 2 0 0 1-2 2A16 16 0 0 1 3 5a2 2 0 0 1 2-2z"/></svg>
          <span>555 301 7284</span>
        </li>
        <li>
          <svg viewBox="0 0 24 24" fill="none" stroke="#3d3d3f" stroke-width="1.6"><rect x="3" y="5" width="18" height="14"/><path d="M3 5l9 8 9-8M3 19l7-7M21 19l-7-7"/></svg>
          <span>dara@whitmorecpa.example</span>
        </li>
        <li>
          <svg viewBox="0 0 24 24" fill="none" stroke="#3d3d3f" stroke-width="1.6"><circle cx="12" cy="12" r="9"/><path d="M3 12h18M12 3c3 3 3 15 0 18M12 3c-3 3-3 15 0 18M5 7.5h14M5 16.5h14"/></svg>
          <span>www.whitmorecpa.example</span>
        </li>
      </ul>
    </div>

    <div class="band" style="left:689px; top:271px; width:188px; height:40px;"></div>
    <div class="band" style="left:837px; top:271px; width:40px; height:211px;"></div>
    <div class="band" style="left:689px; top:442px; width:188px; height:40px;"></div>
  </section>

  <section class="card card--back" aria-label="Business card, back">
    <div class="brand">
      <div class="brand__name">DARA WHITMORE, CPA, LLC</div>
      <div class="brand__tag">CERTIFIED PUBLIC ACCOUNTANT</div>
    </div>
  </section>

</main>
</body>
</html>
```